Kestrel Signs Facebook Banner Design

Design a facebook banner for a sign company. I would like to have a modern approach to it.

Product Offering:
Signs
Banners
Decals
Commercial Wraps

```html
<!DOCTYPE html>
<html lang="en">
<head>
<meta charset="UTF-8">
<title>Kestrel Signs – Facebook Banner</title>
<link href="https://fonts.googleapis.com/css2?family=Poppins:wght@600;700;800;900&display=swap" rel="stylesheet">
<style>
  :root {
    --stage-blue: #0f3384;
    --brand-red: #ee1c25;
    --ink-dark: #3b3b3d;
    --ink-black: #111111;
    --card-grey: #5d5e62;
    --paper: #ffffff;
  }
  html, body {
    margin: 0;
    padding: 0;
    width: 1200px;
    height: 1200px;
    overflow: hidden;
    background: var(--stage-blue);
  }
  .stage {
    position: relative;
    width: 1200px;
    height: 1200px;
  }
  .cover-banner {
    position: absolute;
    left: 118px;
    top: 421px;
    width: 964px;
    height: 357px;
    display: block;
    font-family: "Poppins", sans-serif;
  }
  .headline { font-weight: 800; }
  .headline--red { fill: var(--brand-red); }
  .headline--dark { fill: var(--ink-dark); }
  .services-title { font-weight: 700; }
  .card-label { font-weight: 800; fill: var(--paper); }
  .contact-phone { font-weight: 800; fill: var(--brand-red); }
  .contact-web { font-weight: 800; fill: var(--ink-dark); }
  .badge-number { font-weight: 900; fill: var(--brand-red); }
  .badge-years { font-weight: 800; fill: var(--brand-red); }
  .badge-experience { font-weight: 800; fill: var(--ink-dark); }
</style>
</head>
<body>
<main class="stage">
  <svg class="cover-banner" viewBox="0 0 964 357" xmlns="http://www.w3.org/2000/svg">
    <defs>
      <linearGradient id="workshopTone" x1="0" y1="0" x2="1" y2="0.25">
        <stop offset="0" stop-color="#c3c7cc"/>
        <stop offset="0.18" stop-color="#8d939b"/>
        <stop offset="0.38" stop-color="#b7a98f"/>
        <stop offset="0.52" stop-color="#d4cbb8"/>
        <stop offset="0.66" stop-color="#4b5160"/>
        <stop offset="0.82" stop-color="#2e3340"/>
        <stop offset="1" stop-color="#8a93a3"/>
      </linearGradient>
      <linearGradient id="signsTone" x1="0" y1="0" x2="0" y2="1">
        <stop offset="0" stop-color="#8b8f96"/>
        <stop offset="1" stop-color="#4f6b45"/>
      </linearGradient>
      <linearGradient id="bannersTone" x1="0" y1="0" x2="0" y2="1">
        <stop offset="0" stop-color="#d8dadc"/>
        <stop offset="1" stop-color="#9fb4b8"/>
      </linearGradient>
      <linearGradient id="decalsTone" x1="0" y1="0" x2="1" y2="1">
        <stop offset="0" stop-color="#7a5a3e"/>
        <stop offset="1" stop-color="#c9c2b6"/>
      </linearGradient>
      <linearGradient id="wrapsTone" x1="0" y1="0" x2="0" y2="1">
        <stop offset="0" stop-color="#5e8fd0"/>
        <stop offset="1" stop-color="#2aa6c8"/>
      </linearGradient>
    </defs>

    <rect class="banner-base" x="0" y="0" width="964" height="357" fill="var(--paper)"/>

    <polygon class="hero-photo" role="img" aria-label="Photo of a print technician in dark overalls feeding a sheet into a printing press, with stacks of colourful prints behind"
      points="613,0 964,0 964,357 613,357 526,178" fill="url(#workshopTone)"/>
    <polyline class="hero-edge" points="612,-2 524,178 612,359" fill="none" stroke="var(--brand-red)" stroke-width="6"/>

    <g class="experience-badge">
      <path d="M807,13 H964 V82 H807 Q796,82 796,71 V24 Q796,13 807,13 Z" fill="var(--paper)"/>
      <text class="badge-number" x="812" y="66" font-size="52">5</text>
      <text class="badge-years" x="849" y="48" font-size="28" textLength="99" lengthAdjust="spacingAndGlyphs">YEARS</text>
      <text class="badge-experience" x="847" y="66" font-size="15" textLength="101" lengthAdjust="spacingAndGlyphs">EXPERIENCE</text>
    </g>

    <text class="headline headline--red" x="39" y="66" font-size="48" textLength="460" lengthAdjust="spacingAndGlyphs">TOP SIGN DESIGNS &amp;</text>
    <text class="headline headline--dark" x="38" y="109" font-size="50" textLength="462" lengthAdjust="spacingAndGlyphs">PRINTING EXPERTS</text>

    <text class="services-title" x="63" y="140" font-size="25" textLength="183" lengthAdjust="spacingAndGlyphs"><tspan fill="var(--ink-black)">OUR </tspan><tspan fill="var(--brand-red)">SERVICES</tspan></text>

    <g class="service-card">
      <polygon points="55,149 163,149 142,263 33,263" fill="var(--brand-red)"/>
      <polygon role="img" aria-label="Photo of storefront and pylon signs" points="58,153 158,153 144,228 44,228" fill="url(#signsTone)"/>
      <text class="card-label" x="89" y="251" font-size="11" text-anchor="middle">SIGNS</text>
    </g>
    <g class="service-card">
      <polygon points="167,149 275,149 254,263 145,263" fill="var(--card-grey)"/>
      <polygon role="img" aria-label="Photo of roll-up and feather banners" points="170,153 270,153 256,226 156,226" fill="url(#bannersTone)"/>
      <text class="card-label" x="201" y="249" font-size="11" text-anchor="middle">BANNERS</text>
    </g>
    <g class="service-card">
      <polygon points="279,149 387,149 366,263 257,263" fill="var(--brand-red)"/>
      <polygon role="img" aria-label="Photo of colourful vinyl sticker decals" points="282,153 382,153 368,228 268,228" fill="url(#decalsTone)"/>
      <text class="card-label" x="313" y="251" font-size="11" text-anchor="middle">DECALS</text>
    </g>
    <g class="service-card">
      <polygon points="391,149 499,149 478,263 369,263" fill="var(--card-grey)"/>
      <polygon role="img" aria-label="Photo of a pickup truck with a full vehicle wrap" points="394,153 494,153 482,214 382,214" fill="url(#wrapsTone)"/>
      <text class="card-label" x="425" y="240" font-size="11" text-anchor="middle">COMMERCIALS</text>
      <text class="card-label" x="425" y="253" font-size="11" text-anchor="middle">WRAPS</text>
    </g>

    <text class="contact-phone" x="222" y="314" font-size="40" textLength="250" lengthAdjust="spacingAndGlyphs">(604) 555-0147</text>
    <text class="contact-web" x="223" y="337" font-size="20" textLength="247" lengthAdjust="spacingAndGlyphs">WWW.KESTRELSIGNS.CA</text>
  </svg>
</main>
</body>
</html>
```